PIXEL ART tool bar buttons for female oriented social networking and dating site

Design icons for a high end dating site with a feminine aesthetic similar to the le soir brun tavelle commercial. http://www.clipvoro.example/watch?v=Qx7mReT2kPa

We are looking for small scalable buttons for our tool bar of a man and woman alone and also meeting. Also a magnifying glass.

For the winner we will be negotiating a contract to build an introductory slide show.
Updates

Reason: I'm extending the deadline because nothing remotely useful has been submitted yet and I want to give more detailed specifications to attract more designers

Reason: We will be providing much clearer instructions to the designers. We have learned how to use the system much better.

Target Market(s)

beautiful fashion conscious women, big spenders or aspirational

Industry/Entity Type

Dating

Requirements
Must have
• toolbar graphics must scale down to very small size especially for mobile. THIS IS ONLY FOR AN EXCELLENT PIXEL ART DESIGNER.

```html
<!DOCTYPE html>
<html lang="en">
<head>
<meta charset="utf-8">
<title>Toolbar Buttons</title>
<link rel="stylesheet" href="https://fonts.googleapis.com/css2?family=Arimo:ital,wght@1,700&display=swap">
<style>
  :root {
    --page: #ffffff;
    --tile: #f6b6e6;
    --tile-shadow: rgba(60, 60, 60, 0.45);
    --ink: #111111;
    --swirl-purple: #5a2d8e;
    --swirl-pink: #e6197f;
    --icon-grey: #4a4a4a;
    --icon-light: #c9c9c9;
    --lens: #bfe6f2;
    --bar-red: #e3202a;
    --bar-red-light: #f3666b;
    --bar-red-dark: #a5121a;
    --search-grey: #c4c4c4;
    --search-edge: #8a8a8a;
  }
  html, body { margin: 0; padding: 0; overflow: hidden; background: var(--page); }
  .canvas { position: relative; width: 1200px; height: 900px; overflow: hidden; background: var(--page); font-family: "Arimo", Arial, sans-serif; }

  .button { position: absolute; width: 196px; }
  .button-label { display: block; text-align: center; font-style: italic; font-weight: 700; font-size: 25px; color: var(--ink); line-height: 30px; height: 30px; margin-bottom: 6px; }
  .tile { position: relative; width: 196px; height: 184px; border-radius: 42px; background: var(--tile); box-shadow: 12px 12px 10px var(--tile-shadow); display: flex; align-items: center; justify-content: center; }
  .swirl { position: absolute; left: -72px; top: 110px; width: 120px; height: 150px; border-radius: 50%; background: radial-gradient(ellipse at center, rgba(90,45,142,0.22), rgba(90,45,142,0) 70%); z-index: -1; }

  .art { width: 140px; height: 140px; border-radius: 18px; }
  .art-face { background: linear-gradient(160deg, #f7cdea, #eaa6d6); }
  .art-hand { background: linear-gradient(160deg, #d8d8d8, #6e6e6e); }
  .art-mail { background: linear-gradient(160deg, #8a8a8a, #3f3f3f); }

  .dollar { font-family: "Arimo", Arial, sans-serif; font-weight: 700; font-size: 150px; line-height: 1; color: var(--icon-grey); text-shadow: 6px 6px 6px rgba(0,0,0,0.3); }

  .big-swirl { position: absolute; left: 960px; top: 380px; width: 200px; height: 200px; border-radius: 50%; background: radial-gradient(circle at 55% 45%, rgba(230,25,127,0.28), rgba(230,25,127,0) 70%); }

  .toolbar { position: absolute; left: 16px; top: 736px; width: 1164px; height: 84px; border-radius: 6px; background: linear-gradient(to bottom, var(--bar-red-light), var(--bar-red) 35%, var(--bar-red) 70%, var(--bar-red-dark)); box-shadow: 0 3px 4px rgba(0,0,0,0.3); }
  .mini-buttons { position: absolute; left: 300px; top: 10px; display: flex; gap: 26px; }
  .mini { width: 46px; text-align: center; }
  .mini-label { display: block; font-style: italic; font-weight: 700; font-size: 7px; line-height: 9px; color: var(--ink); white-space: nowrap; }
  .mini-tile { width: 46px; height: 46px; border-radius: 11px; background: var(--tile); box-shadow: 3px 3px 3px var(--tile-shadow); display: flex; align-items: center; justify-content: center; font-weight: 700; color: var(--icon-grey); font-size: 28px; }
  .mini-art { width: 30px; height: 30px; border-radius: 6px; }
  .search-field { position: absolute; left: 848px; top: 14px; width: 280px; height: 54px; background: var(--search-grey); border: 3px solid var(--search-edge); box-sizing: border-box; }
</style>
</head>
<body>
<main class="canvas">

  <div class="button" style="left:116px; top:44px;">
    <span class="button-label">about me</span>
    <div class="swirl" role="img" aria-label="purple swirl ornament"></div>
    <div class="tile"><div class="art art-face" role="img" aria-label="line drawing of a woman in profile"></div></div>
  </div>

  <div class="button" style="left:400px; top:44px;">
    <span class="button-label">now</span>
    <div class="swirl" role="img" aria-label="purple swirl ornament"></div>
    <div class="tile"><div class="art art-hand" role="img" aria-label="hand pointing down"></div></div>
  </div>

  <div class="button" style="left:690px; top:44px;">
    <span class="button-label">mailbox</span>
    <div class="swirl" role="img" aria-label="purple swirl ornament"></div>
    <div class="tile"><div class="art art-mail" role="img" aria-label="grey mailbox with flag"></div></div>
  </div>

  <div class="button" style="left:970px; top:44px;">
    <span class="button-label">people search</span>
    <div class="swirl" role="img" aria-label="purple swirl ornament"></div>
    <div class="tile">
      <svg width="150" height="150" viewBox="0 0 150 150" aria-hidden="true">
        <line x1="70" y1="78" x2="22" y2="132" stroke="#7a7a7a" stroke-width="14" stroke-linecap="round"/>
        <circle cx="92" cy="56" r="40" fill="var(--lens)" stroke="#9a9a9a" stroke-width="9"/>
        <ellipse cx="80" cy="42" rx="14" ry="8" fill="#ffffff" opacity="0.7"/>
      </svg>
    </div>
  </div>

  <div class="button" style="left:116px; top:324px;">
    <span class="button-label">calendar</span>
    <div class="swirl" role="img" aria-label="purple swirl ornament"></div>
    <div class="tile">
      <svg width="140" height="150" viewBox="0 0 140 150" aria-hidden="true">
        <rect x="14" y="24" width="112" height="116" fill="#ffffff" stroke="#9a9a9a" stroke-width="2"/>
        <rect x="14" y="24" width="112" height="14" fill="#8a8a8a"/>
        <circle cx="44" cy="22" r="10" fill="none" stroke="#5a5a5a" stroke-width="4"/>
        <circle cx="96" cy="22" r="10" fill="none" stroke="#5a5a5a" stroke-width="4"/>
        <text x="70" y="82" text-anchor="middle" font-family="Arimo, Arial, sans-serif" font-weight="700" font-size="40" fill="#111">25</text>
        <text x="70" y="124" text-anchor="middle" font-family="Arimo, Arial, sans-serif" font-weight="700" font-size="38" fill="#111">Dec</text>
      </svg>
    </div>
  </div>

  <div class="button" style="left:400px; top:324px;">
    <span class="button-label">currency</span>
    <div class="swirl" role="img" aria-label="purple swirl ornament"></div>
    <div class="tile"><span class="dollar">$</span></div>
  </div>

  <div class="button" style="left:690px; top:324px;">
    <span class="button-label">favs</span>
    <div class="swirl" role="img" aria-label="purple swirl ornament"></div>
    <div class="tile">
      <svg width="150" height="140" viewBox="0 0 150 140" aria-hidden="true">
        <path d="M30 80 A45 50 0 0 1 120 80" fill="none" stroke="var(--icon-grey)" stroke-width="10"/>
        <rect x="16" y="70" width="28" height="44" rx="12" fill="var(--icon-grey)"/>
        <rect x="106" y="70" width="28" height="44" rx="12" fill="var(--icon-grey)"/>
        <path d="M36 110 Q46 132 80 128" fill="none" stroke="var(--icon-grey)" stroke-width="5"/>
        <rect x="78" y="122" width="18" height="10" rx="5" fill="var(--icon-grey)"/>
      </svg>
    </div>
  </div>

  <div class="big-swirl" role="img" aria-label="large pink swirl ornament"></div>

  <nav class="toolbar">
    <div class="mini-buttons">
      <div class="mini"><span class="mini-label">about me</span><div class="mini-tile"><div class="mini-art art-face" role="img" aria-label="woman in profile"></div></div></div>
      <div class="mini"><span class="mini-label">now</span><div class="mini-tile"><div class="mini-art art-hand" role="img" aria-label="pointing hand"></div></div></div>
      <div class="mini"><span class="mini-label">mailbox</span><div class="mini-tile"><div class="mini-art art-mail" role="img" aria-label="mailbox"></div></div></div>
      <div class="mini"><span class="mini-label">calendar</span><div class="mini-tile" style="font-size:14px; color:#111; background:#fff; border:2px solid var(--tile);">25</div></div>
      <div class="mini"><span class="mini-label">currency</span><div class="mini-tile">$</div></div>
      <div class="mini"><span class="mini-label">favs</span><div class="mini-tile">
        <svg width="32" height="30" viewBox="0 0 150 140" aria-hidden="true"><path d="M30 80 A45 50 0 0 1 120 80" fill="none" stroke="#4a4a4a" stroke-width="12"/><rect x="16" y="70" width="28" height="44" rx="12" fill="#4a4a4a"/><rect x="106" y="70" width="28" height="44" rx="12" fill="#4a4a4a"/></svg>
      </div></div>
      <div class="mini"><span class="mini-label">people search</span><div class="mini-tile">
        <svg width="32" height="32" viewBox="0 0 150 150" aria-hidden="true"><line x1="70" y1="78" x2="22" y2="132" stroke="#7a7a7a" stroke-width="16" stroke-linecap="round"/><circle cx="92" cy="56" r="40" fill="#bfe6f2" stroke="#9a9a9a" stroke-width="10"/></svg>
      </div></div>
    </div>
    <div class="search-field" role="search" aria-label="search"></div>
  </nav>

</main>
</body>
</html>
```